" Possui corretores credenciados que vendem lotes e terrenos no Vale do Paraíba. A empresa não possui escritório próprio, os corretores trabalham nos plantões de vendas das incorporadoras. "

```html
<!DOCTYPE html>
<html lang="pt-BR">
<head>
<meta charset="UTF-8">
<title>Vellora Imóveis — Envelope</title>
<link href="https://fonts.googleapis.com/css2?family=Montserrat:wght@400;500&display=swap" rel="stylesheet">
<style>
  :root {
    --page-bg: #eeeeec;
    --envelope-dark: #2b2b2b;
    --brand-yellow: #f6b52a;
    --text-light: #ffffff;
    --text-soft: #e4e4e4;
    --shade: #353535;
  }
  * { margin: 0; padding: 0; box-sizing: border-box; }
  html, body {
    width: 1200px; height: 1200px; overflow: hidden;
    background: var(--page-bg);
    font-family: "Montserrat", sans-serif;
  }
  .envelope {
    position: absolute; left: 100px; top: 372px;
    width: 1000px; height: 450px;
    background: var(--envelope-dark);
    overflow: hidden;
    box-shadow: 0 6px 18px rgba(0,0,0,0.18);
  }
  .envelope__flap { position: absolute; left: 0; top: 0; width: 1000px; height: 30px; }
  .envelope__base-band {
    position: absolute; left: 103px; right: 0; bottom: 0; height: 18px;
    background: var(--brand-yellow);
    border-top-left-radius: 18px;
  }
  .envelope__accent {
    position: absolute; left: 690px; top: 110px;
    width: 240px; height: 240px;
    background: var(--shade);
    border-radius: 18px;
  }
  .brand {
    position: absolute; left: 0; width: 1000px; top: 120px;
    text-align: center; color: var(--text-light); font-weight: 500;
  }
  .brand__mark {
    display: block; width: 84px; height: 84px; margin: 0 auto 44px;
    background: var(--brand-yellow);
  }
  .brand__name { font-size: 50px; letter-spacing: 1px; line-height: 1; }
  .brand__tagline { font-size: 24px; letter-spacing: 12px; margin-top: 10px; padding-left: 12px; line-height: 1; }
  .contacts {
    position: absolute; left: 0; top: 392px; width: 1000px;
    font-size: 15px; color: var(--text-soft);
  }
  .contact { position: absolute; display: flex; align-items: flex-start; gap: 10px; line-height: 20px; }
  .contact--phone { left: 124px; }
  .contact--email { left: 299px; }
  .contact--social { left: 534px; }
  .contact--address { left: 714px; }
  .contact__icon { width: 20px; height: 20px; flex: none; }
</style>
</head>
<body>
  <section class="envelope">
    <svg class="envelope__flap" viewBox="0 0 1000 30" aria-hidden="true">
      <polygon points="0,0 1000,0 1000,30 22,30" fill="var(--brand-yellow)"/>
      <polygon points="975,0 1000,0 1000,30" fill="#e0a21f"/>
    </svg>
    <div class="envelope__accent" aria-hidden="true"></div>

    <div class="brand">
      <span class="brand__mark" aria-hidden="true"></span>
      <div class="brand__name">VELLORA</div>
      <div class="brand__tagline">IMÓVEIS</div>
    </div>

    <div class="contacts">
      <div class="contact contact--phone">
        <svg class="contact__icon" viewBox="0 0 20 20" aria-hidden="true">
          <circle cx="10" cy="10" r="10" fill="var(--brand-yellow)"/>
          <path d="M7 5.5l1.8 2.3-1 1.2a7 7 0 0 0 3.2 3.2l1.2-1 2.3 1.8-1 1.5c-3.5 0-7.5-4-7.5-7.5z" fill="var(--envelope-dark)"/>
        </svg>
        <span>(00) 0000-0000</span>
      </div>
      <div class="contact contact--email">
        <svg class="contact__icon" viewBox="0 0 20 20" aria-hidden="true">
          <circle cx="10" cy="10" r="10" fill="var(--brand-yellow)"/>
          <rect x="5.5" y="6.8" width="9" height="6.4" fill="var(--envelope-dark)"/>
          <path d="M5.5 6.8l4.5 3.6 4.5-3.6" stroke="var(--brand-yellow)" stroke-width="1" fill="none"/>
        </svg>
        <span>velloraimoveis@email.com</span>
      </div>
      <div class="contact contact--social">
        <svg class="contact__icon" viewBox="0 0 20 20" aria-hidden="true">
          <circle cx="10" cy="10" r="10" fill="var(--brand-yellow)"/>
        </svg>
        <span>@velloraimoveis</span>
      </div>
      <div class="contact contact--address">
        <svg class="contact__icon" viewBox="0 0 20 20" aria-hidden="true">
          <circle cx="10" cy="10" r="10" fill="var(--brand-yellow)"/>
          <path d="M10 4.5a3.6 3.6 0 0 0-3.6 3.6c0 2.7 3.6 7 3.6 7s3.6-4.3 3.6-7A3.6 3.6 0 0 0 10 4.5z" fill="var(--envelope-dark)"/>
          <circle cx="10" cy="8.1" r="1.3" fill="var(--brand-yellow)"/>
        </svg>
        <span>Endereço aqui, nº 00<br>Cidade - UF</span>
      </div>
    </div>

    <div class="envelope__base-band" aria-hidden="true"></div>
  </section>
</body>
</html>
```